Create a banner for me that embodies my health and well being package.

I am an intuitive counselor with a busy practice helping clients to shift their blocks and move forward in their lives.
I have created a package called '9 paths home again'
I am wanting a banner to put on my website page, facebook page and to use as a letter head in mailouts.
My ideal clients are those who want to create change in their lives and who invest money in themselves and their personal and spiritual growth.
I am different to regular life coaches as my sessions have a spiritual twist to them creating much deeper change in my clients.
I would like the banner to be mainly font with the title of the progam: 9 Paths Home Again (no other wording) (something along the lines of the Blackjack font) and that ties in with the theme of my website. I'm not sure what else I want with it and am looking for ideas.
Website:
www.brightwillowhealing.com.au
I also have a current facebook page for the business:
https://www.facebook.com/Brightwillow-Healing-Studio-502718364091547/
(Note: I am about to drop my logo and business name and move to using my own name - the rest of the website will remain the same).
I have attached a doc with the draft of what wording will be on the website page any advertising will link to, to give you an idea of what the program is about.

Target Market(s)

People who invest money on themselves who are looking to improve their emotional well being and creating change in their life. Majority are middle aged women (also younger females and some men)

Industry/Entity Type

Health And Wellness

Font styles to use
Other font styles liked:
• I like Blackjack and Amienne. Along those lines.

Requirements
Must have
• Attractive, modern and GREAT font.
Nice to have
• Surprise me with something amazing!
• I love the colours in the 2 images I have up loaded as they represent the heart chakra colours. They could be a feature on the banner or blurred into the background.
Should not have
• Even though my work is quite spiritual I don't want it to look woo woo (meaning airy fairy spiritual stuff!)

```html
<!DOCTYPE html>
<html lang="en">
<head>
<meta charset="utf-8">
<title>9 Paths Home Again — Banner</title>
<link rel="stylesheet" href="https://fonts.googleapis.com/css2?family=Satisfy&family=Dancing+Script:wght@400&display=block">
<style>
  :root {
    --page-bg: #f4f4f2;
    --leaf-deep: #26381a;
    --leaf-mid: #5a7a2e;
    --leaf-light: #8fa84a;
    --blossom: #e07aa8;
    --blossom-soft: #f0b3cf;
    --title-ink: #ffffff;
  }
  * { margin: 0; padding: 0; box-sizing: border-box; }
  html, body {
    width: 1200px;
    height: 1000px;
    overflow: hidden;
    background: var(--page-bg);
  }
  .canvas {
    width: 1200px;
    height: 1000px;
    display: flex;
    align-items: center;
    justify-content: center;
  }
  .banner {
    position: relative;
    width: 1100px;
    height: 422px;
    overflow: hidden;
  }
  .banner-backdrop {
    position: absolute;
    inset: 0;
    background:
      radial-gradient(ellipse 34% 58% at 78% 30%, var(--blossom-soft) 0%, var(--blossom) 38%, rgba(224,122,168,0) 100%),
      radial-gradient(ellipse 22% 40% at 92% 80%, rgba(224,122,168,0.7) 0%, rgba(224,122,168,0) 100%),
      radial-gradient(ellipse 40% 55% at 38% 12%, var(--leaf-light) 0%, rgba(143,168,74,0) 100%),
      radial-gradient(ellipse 45% 60% at 50% 90%, rgba(90,122,46,0.9) 0%, rgba(90,122,46,0) 100%),
      linear-gradient(90deg, var(--leaf-deep) 0%, var(--leaf-mid) 45%, #6f7d3a 70%, #9a6a6e 100%);
  }
  .banner-title {
    position: absolute;
    left: 60px;
    right: 60px;
    top: 50%;
    transform: translateY(-45%);
    text-align: center;
    font-family: "Satisfy", "Dancing Script", cursive;
    font-weight: 400;
    font-size: 112px;
    line-height: 1.2;
    color: var(--title-ink);
    text-shadow: 2px 3px 4px rgba(0, 0, 0, 0.35);
    white-space: nowrap;
  }
</style>
</head>
<body>
  <main class="canvas">
    <section class="banner">
      <div class="banner-backdrop" role="img" aria-label="Softly blurred garden photograph in leafy greens with a pink blossom glowing at the right"></div>
      <h1 class="banner-title">9 Paths Home Again</h1>
    </section>
  </main>
</body>
</html>
```